Jornadas Quietud

I want a Catholic flyer, with the Virgen Mary showing aiding, praying, and Jesus carrying the cross, to invite people to a silent retreat. The retreats are monthly. For women, they are Feb. 21, March 21, etc (every third Saturday), and for men they are Feb. 28, March 28, etc (every fourth Saturday). I want each month date to show for both women and men. Our logo should be in there, which is similar to the Holy family icon attached. Also, show that cost is $80, and the place for the retreats is Casa de Reposo, 4175 Marwick Ln, Falls Church, VA and for more information to contact, for women 540-627-1954 and for men 571-482-7105. I will use the flyer for around 4 x 6 or 3 x 5 postcard. Organizers are: Casas de Monte Olvera. The flyer needs to be in spanish "RETIROS EN SILENCIO" and the months should be labeled in Spanish too.

```html
<!DOCTYPE html>
<html lang="es">
<head>
<meta charset="utf-8">
<title>Retiros en Silencio – Casas de Monte Olvera</title>
<link rel="stylesheet" href="https://fonts.googleapis.com/css2?family=Figtree:wght@500;600&family=Yeseva+One&display=swap">
<style>
  :root {
    --red: #c8243a;
    --red-deep: #8e1424;
    --ink: #231f20;
    --gold: #e8a52c;
    --gold-line: #c9a24a;
    --crimson: #b8213b;
    --white: #ffffff;
  }
  * { margin: 0; padding: 0; box-sizing: border-box; }
  html, body { width: 800px; height: 1200px; overflow: hidden; background: var(--ink); }
  .flyer {
    position: relative; width: 800px; height: 1200px; overflow: hidden;
    font-family: "Figtree", sans-serif; font-weight: 500; color: var(--white);
  }
  .hero-art {
    position: absolute; left: 0; top: 0; width: 800px; height: 758px;
    background: radial-gradient(ellipse at 55% 40%, #b81f33 0%, var(--red) 45%, #b51c31 100%),
                linear-gradient(180deg, var(--red), var(--red-deep));
  }
  .lower-band { position: absolute; left: 0; top: 758px; width: 800px; height: 442px; background: var(--ink); }
  .frame {
    position: absolute; left: 50px; top: 50px; width: 700px; height: 1100px;
    border: 2px solid var(--gold-line); border-radius: 8px;
  }
  .emblem { position: absolute; left: 77px; top: 73px; width: 206px; height: 377px; }
  .display { font-family: "Yeseva One", serif; font-weight: 400; }
  .title {
    position: absolute; right: 74px; top: 68px; text-align: right;
    font-size: 76px; line-height: 90px; letter-spacing: -2.5px;
  }
  .organizer { position: absolute; right: 74px; top: 236px; font-size: 31px; font-weight: 600; }
  .invite {
    position: absolute; right: 78px; top: 301px; text-align: right;
    font-size: 20.5px; line-height: 26.5px;
  }
  .col-head { position: absolute; top: 492px; font-size: 32px; line-height: 40px; letter-spacing: -0.8px; }
  .col-text { position: absolute; top: 530px; font-size: 20.5px; line-height: 27px; }
  .place-head { left: 77px; } .place-text { left: 77px; }
  .cost-head { left: 347px; } .info-head { left: 503px; } .info-text { left: 503px; }
  .label { color: var(--gold); }
  .price {
    position: absolute; left: 335px; top: 535px; width: 130px; height: 79px;
    border: 2px solid var(--gold-line); border-radius: 12px;
    display: flex; align-items: center; justify-content: center;
    font-size: 52px;
  }
  .closing { position: absolute; left: 87px; top: 666px; font-size: 20.5px; line-height: 27px; }
  .dates-title {
    position: absolute; left: 0; width: 800px; top: 776px; text-align: center;
    font-size: 38px; color: var(--crimson);
  }
  .schedule { position: absolute; left: 0; width: 800px; text-align: center; font-size: 21px; line-height: 26.7px; }
  .schedule-women { top: 838px; } .schedule-men { top: 966px; }
  .contact-line {
    position: absolute; left: 0; width: 800px; top: 1096px;
    display: flex; justify-content: center; align-items: center; gap: 8px; font-size: 21px;
  }
  .contact-line .email { color: var(--gold); }
</style>
</head>
<body>
<main class="flyer">
  <div class="hero-art" role="img" aria-label="Ilustración de Jesús cargando la cruz rodeado de una multitud, en tonos rojos"></div>
  <div class="lower-band"></div>
  <div class="frame"></div>

  <svg class="emblem" viewBox="0 0 206 377">
    <defs>
      <linearGradient id="goldCross" x1="0" x2="1">
        <stop offset="0" stop-color="#c9982e"/><stop offset=".5" stop-color="#f3d274"/><stop offset="1" stop-color="#c9982e"/>
      </linearGradient>
      <linearGradient id="iconTone" x1="0" y1="0" x2="0" y2="1">
        <stop offset="0" stop-color="#c49a3a"/><stop offset=".45" stop-color="#b4302a"/><stop offset="1" stop-color="#d46a2a"/>
      </linearGradient>
    </defs>
    <rect x="94" y="0" width="16" height="90" fill="url(#goldCross)"/>
    <rect x="63" y="33" width="79" height="16" fill="url(#goldCross)"/>
    <polygon points="103,86 206,146 206,377 0,377 0,146" fill="#7a6a3c"/>
    <polygon points="103,104 190,154 190,362 16,362 16,154" fill="url(#iconTone)" role="img" aria-label="Icono de la Sagrada Familia: María, José y el Niño Jesús"/>
  </svg>

  <h1 class="title display">RETIROS EN<br>SILENCIO</h1>
  <p class="organizer">Casas de Monte Olvera</p>
  <p class="invite">Ven y encuentra la paz en el silencio<br>con la Virgen María y Jesús.<br>Un día de retiro para renovar tu corazón<br>y fortalecer tu fe.</p>

  <h2 class="col-head place-head display">Lugar:</h2>
  <p class="col-text place-text">Casa de Reposo<br>4175 Marwick<br>Ln, Falls Church, VA</p>

  <h2 class="col-head cost-head display">Costo:</h2>
  <div class="price display">$80</div>

  <h2 class="col-head info-head display">Información:</h2>
  <p class="col-text info-text"><span class="label">Mujeres:</span><br>540-627-1954<br><span class="label">Hombres:</span><br>571-482-7105</p>

  <p class="closing">Con la Virgen María intercediendo y Jesús cargando la<br>cruz, vivamos juntos un encuentro de fe, oración y silencio.</p>

  <h2 class="dates-title display">Fechas de Retiros</h2>
  <div class="schedule schedule-women">
    <p class="label">Para Mujeres – Cada tercer sábado del mes</p>
    <p>17 Enero • 21 Febrero • 21 Marzo • 18 Abril • 16 Mayo<br>• 20 Junio • 18 Julio • 15 Agosto • 19 Septiembre<br>• 17 Octubre • 21 Noviembre • 19 Diciembre</p>
  </div>
  <div class="schedule schedule-men">
    <p class="label">Para Hombres – Cada cuarto sábado del mes</p>
    <p>24 Enero • 28 Febrero • 28 Marzo • 25 Abril • 23 Mayo<br>• 27 Junio • 25 Julio • 22 Agosto • 26 Septiembre<br>• 24 Octubre • 28 Noviembre • 26 Diciembre</p>
  </div>

  <p class="contact-line">
    <span>Casas de Monte Olvera</span>
    <svg width="20" height="14" viewBox="0 0 20 14" aria-hidden="true">
      <rect x="1" y="1" width="18" height="12" fill="none" stroke="#c8243a" stroke-width="2"/>
      <polyline points="1,1 10,8 19,1" fill="none" stroke="#c8243a" stroke-width="2"/>
    </svg>
    <span class="email">info@casasdemonteolvera.org</span>
  </p>
</main>
</body>
</html>
```